Non-Dairy Ice Cream Label for Cup & Lid

The label should reflect that it is a Caribbean brand of non-dairy ice-cream. I would like the graphics to present a natural, tropical and forward thinking aesthetic.
Currently our products are purchased by mainly females, so a broader appeal is desired.

We are really looking for an orginal and appealing design.

The following information must be included -
Product Name: Quilo Non-Dairy Ice-Cream and Sorbet
Product Size: 16 oz / 474ml
Nutritional Facts: (see image of existing product package below)
Ingredients: (see image of existing product package below)
Contact Info: quiloltd@fernmail.test
555-014-7263

The label needs to include a logo for the product name - Quilo Non-Dairy Ice-Cream & Sorbet.

An area should be left blank on the label and the lid to receive a flavour name sticker.

Target Market(s)

Everyone. Lactose Intolerant people . Vegans.

Industry/Entity Type

Food Industry

Requirements
Must have
• A space for a flavour label to go and a nutritional facts and ingredients.
Nice to have
• A new logo, The qo logo i would like to keep as my company logo not specific to the ice cream so the ice cream needs its own logo and i do not mind it being fashioned from the first one eg the qo could be two cherries on an ice ceam cone or sundae. I will be using the current logo that is visible on the old design i uploaded fro my company which makes more than one product including the ice cream which i would like to now have its own logo. I hope this is clearer.

```html
<!DOCTYPE html>
<html lang="en">
<head>
<meta charset="utf-8">
<title>Quilo Non-Dairy Ice-Cream and Sorbet – Cup Label</title>
<link href="https://fonts.googleapis.com/css2?family=Josefin+Sans:wght@700&family=Oswald:wght@400;500&family=Roboto:wght@400;700&display=swap" rel="stylesheet">
<style>
  :root {
    --backdrop: #dcb99c;
    --label-brown: #8a4514;
    --label-brown-deep: #7a3b10;
    --band: #a3581f;
    --cream: #ffffff;
    --cherry: #b5121b;
    --ink: #111111;
    --rule: #8a4514;
    --art-light: #f3c6d2;
    --art-soft: #e9b7c4;
  }
  * { box-sizing: border-box; margin: 0; padding: 0; }
  html, body {
    width: 1200px; height: 1086px; overflow: hidden;
    background: var(--backdrop);
  }
  .cup-label {
    position: absolute; left: 30px; top: 325px;
    width: 1140px; height: 435px;
    background: radial-gradient(circle at 52% 45%, var(--label-brown) 0%, var(--label-brown-deep) 100%);
    overflow: hidden;
  }
  .ingredients {
    position: absolute; left: 26px; top: 310px;
    transform: rotate(-90deg); transform-origin: left top;
    width: 300px;
    font: 400 10px/1.2 "Roboto", sans-serif; color: var(--cream);
  }
  .ingredients strong { font-weight: 700; }
  .nutrition { position: absolute; left: 58px; top: 21px; width: 205px; }
  .nutrition-box {
    position: absolute; left: 0; width: 205px;
    background: var(--cream); color: var(--ink);
    font: 400 7.5px/1.3 "Roboto", sans-serif;
    padding: 4px 7px;
  }
  .nutrition-box h2 { font: 700 10.5px/1.3 "Roboto", sans-serif; margin-bottom: 3px; }
  .box-facts { top: 0; height: 46px; }
  .box-amount { top: 53px; height: 41px; }
  .box-table { top: 102px; height: 78px; }
  .box-details { top: 192px; height: 136px; }
  .pair { display: flex; gap: 40px; }
  .table-head { text-align: right; font: 700 9.5px/1.2 "Roboto", sans-serif; padding-right: 22px; margin-bottom: 2px; }
  .table-row {
    display: grid; grid-template-columns: 48px 95px 1fr;
    border-bottom: 1px solid var(--rule); padding: 1px 4px 0;
  }
  .table-row:last-child { border-bottom: none; }
  .quad { display: grid; grid-template-columns: repeat(4, 1fr); padding: 2px 4px; }
  .details-copy { font-size: 6px; line-height: 1.25; padding: 4px 2px; border-bottom: 1px solid var(--rule); }
  .tiny-grid { display: grid; grid-template-columns: repeat(4, 1fr); font-size: 4.5px; line-height: 1.2; padding: 4px 4px; border-bottom: 1px solid var(--rule); }
  .footer-copy { font-size: 6px; padding: 4px 2px; }
  .brand-mark {
    position: absolute; left: 346px; top: 96px;
    width: 100px; height: 100px; border-radius: 50%;
    background: var(--cherry); border: 5px solid var(--cream);
  }
  .brand-name {
    position: absolute; left: 460px; top: 104px;
    font: 700 86px/1 "Josefin Sans", sans-serif;
    letter-spacing: 4px; color: var(--cream);
  }
  .product-type {
    position: absolute; left: 453px; top: 198px;
    font: 500 36px/1 "Oswald", sans-serif; color: var(--cream);
    letter-spacing: 1px;
  }
  .size {
    position: absolute; left: 436px; top: 254px;
    font: 500 21px/1 "Oswald", sans-serif; color: var(--cream);
  }
  .sorbet-pill {
    position: absolute; left: 493px; top: 242px;
    width: 223px; height: 48px; border-radius: 12px;
    background: var(--cream); color: var(--label-brown);
    font: 400 32px/48px "Oswald", sans-serif; text-align: center; letter-spacing: 2px;
  }
  .dairy-free-badge {
    position: absolute; left: 730px; top: 243px;
    width: 52px; height: 52px; border-radius: 50%;
    background: radial-gradient(circle, #f2f2f2 55%, var(--cherry) 58%);
  }
  .art-area {
    position: absolute; top: 272px; height: 163px;
    background: linear-gradient(135deg, var(--art-light) 0%, var(--art-soft) 100%);
    opacity: 0.85;
  }
  .art-left { left: 316px; width: 100px; }
  .art-right { left: 825px; width: 117px; }
  .flavour-band {
    position: absolute; left: 0; top: 365px; width: 100%; height: 38px;
    background: var(--band);
  }
  .flavour-band span {
    position: absolute; top: 0; transform: translateX(-50%);
    font: 400 22px/38px "Oswald", sans-serif; color: var(--cream); letter-spacing: 1.5px;
    white-space: nowrap;
  }
  .contact {
    position: absolute; left: 1098px; top: 306px;
    transform: rotate(-90deg); transform-origin: left top;
    width: 260px;
    font: 400 10.5px/1.2 "Roboto", sans-serif; color: var(--cream);
  }
  .contact strong { font-weight: 700; }
</style>
</head>
<body>
  <section class="cup-label" role="img" aria-label="Brown label background with faint tropical fruit doodles and a large swirl">
    <p class="ingredients"><strong>Ingridients:</strong> Sugar, Milk, Coconut<br>Soy Protein</p>

    <div class="nutrition">
      <div class="nutrition-box box-facts">
        <h2>Nutritional Facts</h2>
        <p>Serving Size: 1/2 cup</p>
        <p>Lorem Ipsome: Lorem Ipsome</p>
      </div>
      <div class="nutrition-box box-amount">
        <h2>Amount Per serving</h2>
        <p class="pair"><span>Lorem Ipsome:</span><span>Lorem Ipsome</span></p>
      </div>
      <div class="nutrition-box box-table">
        <p class="table-head">Lorem</p>
        <p class="table-row"><span>Lorem</span><span>Lorem</span><span>Lorem</span></p>
        <p class="table-row"><span>Lorem</span><span>Lorem</span><span>Lorem</span></p>
        <p class="table-row"><span>Lorem</span><span>Lorem</span><span>Lorem</span></p>
        <p class="table-row"><span>Lorem</span><span>Lorem</span><span>Lorem</span></p>
        <p class="table-row"><span>Lorem</span><span>Lorem</span><span></span></p>
      </div>
      <div class="nutrition-box box-details">
        <p class="quad"><span>Lorem</span><span>Lorem</span><span>Lorem</span><span>Lorem</span></p>
        <p class="details-copy">Lorem ipsum dolor sit amet, consectetuer adipiscing elit, sed diam nonummy nibh euismod tincidunt ut laoreet dolore magna aliquam erat volutpat. Ut wisi enim ad minim veniam, quis nostrud exerci tation</p>
        <div class="tiny-grid">
          <span>Lorem</span><span>Lorem</span><span>Lorem</span><span>Lorem</span>
          <span>Lorem</span><span>Lorem</span><span>Lorem</span><span>Lorem</span>
          <span>Lorem</span><span>Lorem</span><span>Lorem</span><span>Lorem</span>
          <span>Lorem</span><span>Lorem</span><span>Lorem</span><span>Lorem</span>
        </div>
        <p class="footer-copy">Lorem ipsum dolor<br>Lorem &nbsp;&nbsp; Lorem &nbsp;&nbsp; Lorem</p>
      </div>
    </div>

    <div class="art-area art-left" role="img" aria-label="Illustration area: pink ice cream scoop with sprinkles and a cherry on a wafer cone"></div>
    <div class="art-area art-right" role="img" aria-label="Illustration area: pink ice cream scoop with sprinkles and a cherry on a wafer cone"></div>

    <div class="brand-mark"></div>
    <h1 class="brand-name">QUILO</h1>
    <p class="product-type">NON DAIRY ICECREAM</p>
    <p class="size">474ml</p>
    <p class="sorbet-pill">AND SORBET</p>
    <div class="dairy-free-badge" role="img" aria-label="Dairy free badge"></div>

    <div class="flavour-band">
      <span style="left:167px">FLAVOUR LABEL</span>
      <span style="left:369px">FLAVOUR LABEL</span>
      <span style="left:570px">FLAVOUR LABEL</span>
      <span style="left:771px">FLAVOUR LABEL</span>
      <span style="left:973px">FLAVOUR LABEL</span>
    </div>

    <p class="contact"><strong>Contact Info:</strong> quiloltd@fernmail.test<br>555-014-7263</p>
  </section>
</body>
</html>
```